Occupational Therapist does home accessibility for disabled folks; needs business card design

We need a business card for a company in Portland, Oregon that specializes in making homes accessible, comfortable, and functional for people who are disabled or aging who would like to stay in THEIR home. Our medical background as Occupational Therapists allows us to translate the functional needs of the person into the recommendations for the design of the home remodel.

Target Market(s)

Elderly, children of elderly
People with disabilities, families of people with disabilities

Industry/Entity Type

Business

Contact Information for Business Card

Company name: HomeWell
Name: Karen Dwyer Lopez, OTR/L, CAPS, ECHM
Occupational Therapist, Home Modification & Accessibility Specialist
website: www.homewellsteady.com
email: homewellsteady@mailbright.com
phone: (503)418-2957
CCB #: 384517

Font styles to use
Sans Serif

Requirements
Must have
• My logo
• Easy to read font with contrasting background
• Please list the Services offered: Occupational Therapy, Home safety & accessibility assessments, Home modification consulting, project management
Nice to have
• Friendly, welcoming feel
Should not have
• Dark colored background

```html
<!DOCTYPE html>
<html lang="en">
<head>
<meta charset="utf-8">
<title>HomeWell Business Card</title>
<link rel="stylesheet" href="https://fonts.googleapis.com/css2?family=Lato:wght@400;700&display=swap">
<style>
  :root {
    --orange: #d8811f;
    --slate: #5c5c5e;
    --ink: #555558;
    --paper: #f4f4f2;
    --backdrop: #e3e2df;
  }
  * { box-sizing: border-box; margin: 0; padding: 0; }
  html, body { width: 1200px; height: 780px; overflow: hidden; }
  body {
    background: var(--backdrop);
    font-family: "Lato", Arial, sans-serif;
    color: var(--ink);
    position: relative;
  }
  .card {
    position: absolute;
    top: 230px;
    width: 560px;
    height: 320px;
    background: var(--paper);
    box-shadow: 0 6px 18px rgba(0,0,0,0.18);
    overflow: hidden;
  }
  .card--front { left: 20px; }
  .card--back { left: 620px; }

  .band {
    position: absolute;
    left: 0; right: 0; bottom: 0;
    height: 16px;
    display: flex;
  }
  .band__orange { background: var(--orange); }
  .band__slate { background: var(--slate); flex: 1; }
  .card--front .band__orange { width: 42%; }
  .card--back .band__orange { width: 55%; }

  .brand {
    display: flex;
    align-items: center;
    gap: 12px;
    font-weight: 700;
    color: var(--orange);
    letter-spacing: 0.5px;
  }
  .brand__mark {
    width: 34px; height: 34px;
    background: var(--slate);
  }

  /* front */
  .card--front .brand {
    position: absolute;
    left: 170px; top: 78px;
    font-size: 50px;
  }
  .services {
    position: absolute;
    left: 0; right: 0; top: 172px;
    text-align: center;
  }
  .services__title {
    color: var(--orange);
    font-size: 15px;
    font-weight: 700;
    letter-spacing: 0.5px;
    margin-bottom: 8px;
  }
  .services__list {
    font-size: 14.5px;
    line-height: 1.45;
    color: var(--ink);
  }

  /* back */
  .card--back .brand {
    position: absolute;
    right: 28px; top: 70px;
    font-size: 40px;
  }
  .card--back .brand__mark { width: 28px; height: 28px; }
  .person {
    position: absolute;
    left: 30px; top: 138px;
    right: 30px;
  }
  .person__name {
    font-size: 19px;
    font-weight: 700;
    color: var(--ink);
  }
  .person__creds { font-size: 15px; }
  .person__title {
    font-size: 14px;
    padding-bottom: 6px;
    border-bottom: 2px solid var(--orange);
  }
  .contact {
    position: absolute;
    left: 30px; top: 210px;
    list-style: none;
    font-size: 14px;
  }
  .contact__item {
    display: flex;
    align-items: center;
    gap: 8px;
    height: 20px;
  }
  .contact__icon { width: 14px; height: 14px; display: block; }
  .license {
    position: absolute;
    right: 30px; bottom: 34px;
    font-size: 15px;
    color: var(--ink);
  }
</style>
</head>
<body>

  <section class="card card--front">
    <div class="brand"><span class="brand__mark"></span>HomeWell</div>
    <div class="services">
      <p class="services__title">SERVICES OFFERED</p>
      <p class="services__list">Occupational Therapy | Home safety &amp; accessibility assessments<br>Home modification consulting | project management</p>
    </div>
    <div class="band"><span class="band__orange"></span><span class="band__slate"></span></div>
  </section>

  <section class="card card--back">
    <div class="brand"><span class="brand__mark"></span>HomeWell</div>
    <div class="person">
      <p class="person__name">Karen Dwyer Lopez, <span class="person__creds">OTR/L, CAPS, ECHM</span></p>
      <p class="person__title">Occupational Therapist, Home Modification &amp; Accessibility Specialist</p>
    </div>
    <ul class="contact">
      <li class="contact__item">
        <svg class="contact__icon" viewBox="0 0 14 14" aria-hidden="true"><rect width="14" height="14" fill="#d8811f"/><path d="M4 3h2l1 2-1 1c.5 1 1 1.5 2 2l1-1 2 1v2c-4 0-7-3-7-7z" fill="#fff"/></svg>
        (503)418-2957
      </li>
      <li class="contact__item">
        <svg class="contact__icon" viewBox="0 0 14 14" aria-hidden="true"><rect width="14" height="14" fill="#d8811f"/><rect x="3" y="4" width="8" height="6" fill="none" stroke="#fff"/><path d="M3 4l4 3 4-3" fill="none" stroke="#fff"/></svg>
        homewellsteady@mailbright.com
      </li>
      <li class="contact__item">
        <svg class="contact__icon" viewBox="0 0 14 14" aria-hidden="true"><rect width="14" height="14" fill="#d8811f"/><circle cx="7" cy="7" r="4" fill="none" stroke="#fff"/><path d="M3 7h8M7 3c-2 2-2 6 0 8M7 3c2 2 2 6 0 8" fill="none" stroke="#fff" stroke-width=".8"/></svg>
        www.homewellsteady.com
      </li>
    </ul>
    <p class="license">CCB #: 384517</p>
    <div class="band"><span class="band__orange"></span><span class="band__slate"></span></div>
  </section>

</body>
</html>
```